Presentation Box for dry goods meat product

We would like a box designed for presentation on a shelf. Our product is fully cooked meats (beef, pork and chicken) that has a 12- to 18-month shelf-life without refrigeration. It's not dried food, but because of the cooking process it's succulent meat in sauce, storable at room temperature.Our anchor product will be "Hollow Creek Smoke Pit."The dimensions for the box will be approximately 8" tall by 5" wide and 2.5" deep.We have an oval-shaped (horizontal) logo in Navy, Crimson and Old Gold (think Marlow Foxhounds colors).
Updates

Reason: We haven't received enough options. We want the design to say "Hollow Creek Style Smoke Pit" not "Hollow Creek Smoke Pit." Use pictures of beef brisket (not steaks), pulled pork (not pork chops) and pulled chicken (not chicken legs/thighs).

Target Market(s)

Meat-buying consumers

Industry/Entity Type

Cooking

Requirements
Must have
• Space for ingredients and nutrition information. The name of our company is Tellan Foods.
Nice to have
• Picture of Bar-B-Que beef, pork and chicken

```html
<!DOCTYPE html>
<html lang="en">
<head>
<meta charset="utf-8">
<title>Tellan Foods – Hollow Creek Smoke Pit Box</title>
<link href="https://fonts.googleapis.com/css2?family=Open+Sans:ital,wght@0,600;0,700;1,600&family=Roboto+Condensed:wght@700&display=swap" rel="stylesheet">
<style>
  :root {
    --bg-light: #f4f4f4;
    --bg-edge: #d6d6d6;
    --crimson: #c8141c;
    --crimson-dark: #8e0a0f;
    --crimson-soft: #f25a5f;
    --maroon: #7a1a24;
    --maroon-dark: #5a0f16;
    --orange: #f39a1e;
    --orange-dark: #e0820c;
    --navy: #1c2452;
    --white: #ffffff;
    --pink-fade: #f6cfd2;
    --rule: #555555;
    --text-dark: #333333;
    --meat-1: #8a4a22;
    --meat-2: #d9a27a;
    --plate: #f1ece6;
  }
  * { box-sizing: border-box; margin: 0; padding: 0; }
  html, body {
    width: 1079px; height: 1200px; overflow: hidden;
  }
  body {
    background: radial-gradient(ellipse at center, var(--bg-light) 40%, var(--bg-edge) 100%);
    font-family: "Open Sans", sans-serif;
    position: relative;
  }
  .box-net {
    position: absolute;
    left: 200px; top: 200px;
    width: 690px; height: 800px;
    display: flex;
    box-shadow: 0 20px 40px rgba(0,0,0,0.18);
  }

  /* Front panel */
  .front-panel {
    position: relative;
    width: 480px; height: 800px;
    background: var(--white);
    overflow: hidden;
  }
  .brand-area {
    height: 200px;
    display: flex; align-items: center; justify-content: center; gap: 12px;
  }
  .brand-mark {
    width: 18px; height: 18px; border-radius: 50%;
    background: var(--navy);
  }
  .brand-name {
    font-family: "Open Sans", sans-serif;
    font-weight: 700;
    font-size: 44px;
    color: var(--navy);
    letter-spacing: -0.5px;
  }
  .red-field {
    position: absolute; left: 0; top: 170px;
    width: 480px; height: 420px;
    background: linear-gradient(180deg, var(--crimson-soft) 0%, var(--crimson) 30%, var(--crimson-dark) 100%);
    border-radius: 50% 50% 0 0 / 40px 40px 0 0;
  }
  .red-field::before {
    content: ""; position: absolute; left: 0; top: 0; right: 0; height: 50px;
    background: linear-gradient(180deg, var(--pink-fade), transparent);
    border-radius: 50% 50% 0 0 / 40px 40px 0 0;
  }
  .title-banner {
    position: absolute; left: 30px; top: 280px;
    width: 430px;
    transform: rotate(-2deg);
  }
  .tag-region {
    display: inline-block;
    margin-left: 60px;
    background: var(--maroon);
    border: 2px solid var(--white);
    color: var(--white);
    font-weight: 600;
    font-size: 30px;
    padding: 2px 14px;
    position: relative; z-index: 2;
  }
  .title-bar {
    background: linear-gradient(180deg, var(--orange) 0%, var(--orange-dark) 100%);
    border: 2px solid var(--white);
    margin-top: -6px;
    padding: 8px 10px 10px;
    text-align: center;
  }
  .title-main {
    font-family: "Open Sans", sans-serif;
    font-style: italic; font-weight: 600;
    font-size: 62px; line-height: 1;
    color: var(--white);
    text-shadow: 2px 3px 3px rgba(90,20,10,0.55);
  }
  .tag-quality {
    display: inline-block;
    margin: -4px 0 0 56px;
    background: var(--maroon-dark);
    border: 2px solid var(--white);
    color: var(--white);
    font-family: "Roboto Condensed", sans-serif;
    font-weight: 700; font-size: 24px;
    padding: 2px 12px;
  }
  .food-photo {
    position: absolute; left: 0; bottom: 0;
    width: 480px; height: 310px;
    background: radial-gradient(ellipse at 55% 65%, var(--meat-1) 0%, var(--meat-2) 45%, var(--plate) 75%);
  }

  /* Side panel */
  .side-panel {
    position: relative;
    width: 210px; height: 800px;
    background: linear-gradient(180deg, var(--crimson) 0%, var(--crimson-dark) 100%);
    overflow: hidden;
  }
  .side-sheet {
    position: absolute; left: 14px; top: 30px;
    width: 182px; height: 560px;
    background: var(--white);
  }
  .side-banner {
    position: absolute; left: 8px; top: 40px; width: 180px;
    transform: rotate(-8deg); z-index: 2;
  }
  .side-banner .tag-region { font-size: 15px; margin-left: 14px; padding: 1px 6px; }
  .side-banner .title-bar { padding: 3px 4px 5px; margin-top: -3px; }
  .side-banner .title-main { font-size: 30px; }
  .side-banner .tag-quality { font-size: 12px; margin: -2px 0 0 10px; padding: 1px 6px; }
  .info-block {
    position: absolute; left: 22px; width: 150px;
  }
  .info-block.nutrition { top: 170px; }
  .info-block.ingredients { top: 380px; }
  .info-title {
    font-family: "Roboto Condensed", sans-serif;
    font-weight: 700; font-size: 15px;
    color: var(--text-dark);
    text-align: center;
    margin-bottom: 10px;
  }
  .info-lines { display: block; }
  .side-photo {
    position: absolute; left: 0; bottom: 0;
    width: 210px; height: 210px;
    background: radial-gradient(ellipse at 50% 65%, var(--meat-1) 0%, var(--meat-2) 45%, var(--plate) 80%);
  }
</style>
</head>
<body>
  <div class="box-net">
    <section class="front-panel">
      <div class="red-field"></div>
      <header class="brand-area" style="position:relative;z-index:1;">
        <span class="brand-mark"></span>
        <span class="brand-name">Tellan Foods</span>
      </header>
      <div class="title-banner">
        <span class="tag-region">Hollow Creek</span>
        <div class="title-bar"><div class="title-main">Smoke Pit</div></div>
        <span class="tag-quality">Premium quality product</span>
      </div>
      <div class="food-photo" role="img" aria-label="Photo of grilled barbecue meat on a white plate with fresh herbs and a small dish of sauce"></div>
    </section>

    <aside class="side-panel">
      <div class="side-sheet"></div>
      <div class="side-banner">
        <span class="tag-region">Hollow Creek</span>
        <div class="title-bar"><div class="title-main">Smoke Pit</div></div>
        <span class="tag-quality">Premium quality product</span>
      </div>
      <div class="info-block nutrition">
        <div class="info-title">Nutrition information</div>
        <svg class="info-lines" width="150" height="160" viewBox="0 0 150 160">
          <g stroke="var(--rule)" stroke-width="1.5">
            <line x1="0" y1="8" x2="150" y2="8"/><line x1="0" y1="26" x2="150" y2="26"/>
            <line x1="0" y1="44" x2="150" y2="44"/><line x1="0" y1="62" x2="150" y2="62"/>
            <line x1="0" y1="80" x2="150" y2="80"/><line x1="0" y1="98" x2="150" y2="98"/>
            <line x1="0" y1="116" x2="150" y2="116"/><line x1="0" y1="134" x2="150" y2="134"/>
            <line x1="0" y1="152" x2="150" y2="152"/>
          </g>
        </svg>
      </div>
      <div class="info-block ingredients">
        <div class="info-title">Ingredients</div>
        <svg class="info-lines" width="150" height="160" viewBox="0 0 150 160">
          <g stroke="var(--rule)" stroke-width="1.5">
            <line x1="0" y1="8" x2="150" y2="8"/><line x1="0" y1="26" x2="150" y2="26"/>
            <line x1="0" y1="44" x2="150" y2="44"/><line x1="0" y1="62" x2="150" y2="62"/>
            <line x1="0" y1="80" x2="150" y2="80"/><line x1="0" y1="98" x2="150" y2="98"/>
            <line x1="0" y1="116" x2="150" y2="116"/><line x1="0" y1="134" x2="150" y2="134"/>
          </g>
        </svg>
      </div>
      <div class="side-photo" role="img" aria-label="Photo of grilled barbecue meat with herbs and sauce"></div>
    </aside>
  </div>
</body>
</html>
```